Ironvale Beard Oil - Premium Label Design

We need a premium, masculine, and minimalistic label design for our new beard oil brand, Ironvale. The product is crafted with grass-fed beef tallow and essential oils. The design should evoke strength, authenticity, and sophistication, without being too busy. We want a bold, clean look, with the slogan integrated:
“Stand Unbroken. Crafted with Beef Tallow. Forged for Men.”
Please make sure the style is modern and rugged, possibly featuring a monolithic stone element in the background, similar to the inspiration provided in the uploaded file but it need to be sorta completely different.
Updates
I want the label to be able to fit the type of bottle matte black
Industry/Entity Type
Skin Care
Colors
Designer to choose colors to be used in the design.
Requirements
Must have
- Back and front. Creative IRONVALE police design, Beard oil and aftershave mentioned
Nice to have
- grass fed icon, bio icon

```html
<!DOCTYPE html>
<html lang="en">
<head>
<meta charset="utf-8">
<title>Ironvale Beard Oil – Label Front and Back</title>
<link href="https://fonts.googleapis.com/css2?family=Montserrat:wght@400;500;600;700&display=swap" rel="stylesheet">
<style>
  :root {
    --backdrop: #e6e6e6;
    --label: #2a2a2a;
    --label-edge: #1f1f1f;
    --ink: #cfcfcf;
    --ink-soft: #a3a3a3;
    --ink-muted: #858585;
    --art-top: #d0d0d0;
    --art-bottom: #6f6f6f;
  }
  * { box-sizing: border-box; margin: 0; padding: 0; }
  html, body {
    width: 1200px; height: 902px; overflow: hidden;
    background: var(--backdrop);
    font-family: "Montserrat", sans-serif;
  }
  .sheet {
    width: 1200px; height: 902px;
    display: flex; justify-content: center; align-items: center; gap: 70px;
  }
  .label {
    width: 420px; height: 640px;
    background: var(--label);
    border: 1px solid var(--label-edge);
    border-radius: 14px;
    display: flex; flex-direction: column; align-items: center;
    padding: 56px 40px 40px;
    color: var(--ink);
    text-align: center;
  }
  .summit-art {
    width: 250px; height: 190px;
    background: linear-gradient(180deg, var(--art-top), var(--art-bottom));
    border-radius: 4px;
    opacity: .85;
  }
  .brand-name {
    margin-top: 18px;
    font-size: 54px; font-weight: 700; letter-spacing: 2px;
    color: var(--ink);
  }
  .slogan {
    margin-top: 22px;
    font-size: 17px; font-weight: 500; letter-spacing: 6px;
    color: var(--ink-soft);
  }
  .tagline {
    margin-top: 16px;
    font-size: 11px; letter-spacing: 1.5px; line-height: 1.6;
    color: var(--ink-muted);
  }
  .badges {
    margin-top: 22px;
    display: flex; gap: 18px; justify-content: center;
  }
  .badge { display: flex; flex-direction: column; align-items: center; gap: 6px; }
  .badge svg { width: 46px; height: 46px; }
  .badge-name { font-size: 7px; letter-spacing: .8px; color: var(--ink-muted); text-transform: uppercase; }
  .product-type {
    margin-top: auto;
    font-size: 12px; font-weight: 500; letter-spacing: 1px;
    color: var(--ink-soft);
  }
  .emblem {
    width: 84px; height: 84px; margin-top: 40px;
    border-radius: 50%;
    background: linear-gradient(180deg, #5a5a5a, #3c3c3c);
  }
  .back .slogan { margin-top: 28px; }
  .divider { margin-top: 32px; width: 220px; height: 14px; }
  .headline {
    margin-top: 20px;
    font-size: 16px; font-weight: 600; letter-spacing: 3px; line-height: 1.35;
    color: var(--ink);
  }
  .body-copy {
    margin-top: 14px;
    font-size: 9px; letter-spacing: .8px; line-height: 1.55;
    color: var(--ink-muted); text-transform: uppercase;
  }
  .back .badges { gap: 30px; margin-top: 28px; }
  .back .badge svg { width: 40px; height: 40px; }
  .volume { margin-top: auto; font-size: 12px; letter-spacing: 1.5px; color: var(--ink-muted); }
</style>
</head>
<body>
<main class="sheet">

  <section class="label front">
    <div class="summit-art" role="img" aria-label="Illustration of a rugged stone mountain peak"></div>
    <h1 class="brand-name">IRONVALE</h1>
    <p class="slogan">STAND UNBROKEN</p>
    <p class="tagline">CRAFTED WITH BEEF TALLOW.<br>FORGED FOR MEN.</p>
    <div class="badges">
      <div class="badge">
        <svg viewBox="0 0 46 46" role="img" aria-label="Grass-fed badge"><circle cx="23" cy="23" r="21" fill="none" stroke="#a3a3a3" stroke-width="1.5"/><path d="M14 30c4-8 14-8 18 0" fill="none" stroke="#a3a3a3" stroke-width="1.5"/></svg>
        <span class="badge-name">Grass-fed</span>
      </div>
      <div class="badge">
        <svg viewBox="0 0 46 46" role="img" aria-label="Organic leaf badge"><circle cx="23" cy="23" r="21" fill="none" stroke="#a3a3a3" stroke-width="1.5"/><path d="M23 33c-8-4-8-14 0-20 8 6 8 16 0 20z" fill="#a3a3a3"/></svg>
        <span class="badge-name">Organic</span>
      </div>
      <div class="badge">
        <svg viewBox="0 0 46 46" role="img" aria-label="Aromatics drop badge"><circle cx="23" cy="23" r="21" fill="none" stroke="#a3a3a3" stroke-width="1.5"/><path d="M23 12c5 7 8 11 8 15a8 8 0 0 1-16 0c0-4 3-8 8-15z" fill="#a3a3a3"/></svg>
        <span class="badge-name">Aromatics</span>
      </div>
      <div class="badge">
        <svg viewBox="0 0 46 46" role="img" aria-label="Handcrafted badge"><circle cx="23" cy="23" r="21" fill="none" stroke="#a3a3a3" stroke-width="1.5"/><circle cx="23" cy="23" r="9" fill="none" stroke="#a3a3a3" stroke-width="2"/></svg>
        <span class="badge-name">Handcrafted</span>
      </div>
    </div>
    <p class="product-type">BEARD OIL &amp; AFTERSHAVE</p>
  </section>

  <section class="label back">
    <div class="emblem" role="img" aria-label="Round emblem with a bearded man illustration"></div>
    <p class="slogan">STAND UNBROKEN</p>
    <svg class="divider" viewBox="0 0 220 14" aria-hidden="true">
      <path d="M0 6 L90 7 L220 8" stroke="#8a8a8a" stroke-width="1" fill="none"/>
      <path d="M96 7 l7-6 7 6-7 6z M110 7 l7-6 7 6-7 6z" fill="#a3a3a3"/>
    </svg>
    <h2 class="headline">CRAFTED WITH GRASS-FED<br>BEEF TALLOW</h2>
    <p class="body-copy">And enriched with botanical essence, Ironvale is built for the modern man. Use daily as beard oil or aftershave to nourish skin, tame hair, and forge your legacy.</p>
    <div class="badges">
      <div class="badge">
        <svg viewBox="0 0 40 40" role="img" aria-label="Grass-fed icon"><rect x="6" y="12" width="28" height="16" rx="6" fill="#a3a3a3"/></svg>
        <span class="badge-name">Grass-fed</span>
      </div>
      <div class="badge">
        <svg viewBox="0 0 40 40" role="img" aria-label="Recyclable icon"><path d="M20 6 L32 28 H8z" fill="none" stroke="#a3a3a3" stroke-width="3"/></svg>
        <span class="badge-name">Recyclable</span>
      </div>
      <div class="badge">
        <svg viewBox="0 0 40 40" role="img" aria-label="Bio leaf icon"><path d="M20 34c-10-6-10-20 0-28 10 8 10 22 0 28z" fill="#a3a3a3"/></svg>
        <span class="badge-name">Bio</span>
      </div>
      <div class="badge">
        <svg viewBox="0 0 40 40" role="img" aria-label="Essence flask icon"><path d="M16 6h8v10l8 16H8l8-16z" fill="#a3a3a3"/></svg>
        <span class="badge-name">Essence</span>
      </div>
    </div>
    <p class="volume">50 ML / 1.7 FL.OZ</p>
  </section>

</main>
</body>
</html>
```